Gantry Reclaim.com is wanting to create a Chatterloop Ad to attract buyers to come to their website. We are wanting buyers to register for free and create an account on Gantry Reclaim. com. We want to increase the number of buyers by posting an ad on Chatterloop groups. The buyer will click the link to our websites registration page.
https://www.gantryreclaim.com/account/users/register

Semi Trucks
Semi Trailers
Construction Equipment
Farm Equipment
Trailers
ATV/UTV
Boats
RVs

```html
<!DOCTYPE html>
<html lang="en">
<head>
<meta charset="utf-8">
<title>Gantry Reclaim – Buyer Registration Ad</title>
<link rel="stylesheet" href="https://fonts.googleapis.com/css2?family=Poppins:ital,wght@0,500;0,700;0,800;1,800&display=swap">
<style>
  :root {
    --orange: #e8601c;
    --orange-deep: #d9551a;
    --ink: #111111;
    --paper: #ffffff;
    --truck-sky: #8fb3d6;
    --truck-body: #d8d8d2;
    --excavator: #c9a22a;
    --excavator-dark: #4a4a44;
    --dozer: #8c7a58;
    --dozer-mud: #6b5d45;
  }
  * { margin: 0; padding: 0; box-sizing: border-box; }
  html, body { width: 1200px; height: 1200px; overflow: hidden; }
  body {
    background: var(--orange);
    font-family: "Poppins", Arial, sans-serif;
    position: relative;
  }
  .ad-card {
    position: absolute;
    left: 84px; top: 84px;
    width: 1032px; height: 1032px;
    background: var(--paper);
    box-shadow: 0 0 34px rgba(0,0,0,.5);
    overflow: hidden;
  }
  .ad-art {
    position: absolute; left: 0; top: 0;
    width: 1032px; height: 1032px;
  }
  .brand {
    position: absolute;
    left: 38px; top: 48px;
    display: flex; align-items: center; gap: 14px;
  }
  .brand-mark {
    width: 30px; height: 30px;
    background: var(--orange);
  }
  .brand-name {
    font-weight: 800;
    font-size: 38px;
    line-height: 1.02;
    color: var(--ink);
    letter-spacing: -0.5px;
    text-transform: uppercase;
  }
  .headline {
    position: absolute;
    left: 36px; top: 216px;
    font-weight: 800;
    font-size: 70px;
    line-height: 74px;
    letter-spacing: -1.5px;
    text-transform: uppercase;
    color: var(--ink);
  }
  .headline .accent { color: var(--orange); display: block; }
  .headline .plain { display: block; }
  .category-list {
    position: absolute;
    left: 38px; top: 530px;
    list-style: none;
  }
  .category-list li {
    display: flex; align-items: center; gap: 10px;
    font-weight: 500;
    font-size: 32px;
    line-height: 40px;
    color: var(--ink);
    letter-spacing: -0.3px;
  }
  .category-list svg { width: 22px; height: 22px; flex: none; }
  .cta {
    position: absolute;
    left: 0; top: 867px;
    width: 538px; height: 165px;
    display: flex; align-items: center;
    padding-left: 36px;
  }
  .cta-text {
    font-weight: 800;
    font-style: italic;
    font-size: 45px;
    line-height: 48px;
    letter-spacing: -2px;
    color: var(--paper);
    text-transform: uppercase;
  }
</style>
</head>
<body>
  <main class="ad-card">
    <svg class="ad-art" viewBox="0 0 1032 1032" xmlns="http://www.w3.org/2000/svg">
      <defs>
        <linearGradient id="truck-tone" x1="0" y1="0" x2="0" y2="1">
          <stop offset="0" stop-color="var(--truck-sky)"/>
          <stop offset="0.45" stop-color="var(--truck-body)"/>
          <stop offset="1" stop-color="#9c9a92"/>
        </linearGradient>
        <linearGradient id="excavator-tone" x1="0" y1="0" x2="1" y2="0">
          <stop offset="0" stop-color="var(--excavator)"/>
          <stop offset="0.6" stop-color="var(--excavator-dark)"/>
          <stop offset="1" stop-color="#7fa8c9"/>
        </linearGradient>
        <linearGradient id="dozer-tone" x1="0" y1="0" x2="0" y2="1">
          <stop offset="0" stop-color="#8aa16a"/>
          <stop offset="0.4" stop-color="var(--dozer)"/>
          <stop offset="1" stop-color="var(--dozer-mud)"/>
        </linearGradient>
      </defs>
      <polygon class="side-band" points="738,0 1032,0 1032,1032 538,1032" fill="var(--orange)"/>
      <polygon class="side-stripe" points="756,0 772,0 572,1032 556,1032" fill="var(--paper)"/>
      <rect class="cta-band" x="0" y="867" width="548" height="165" fill="var(--orange)"/>

      <g role="img" aria-label="Photo of a white semi truck parked on a gravel lot">
        <polygon points="578,90 1032,90 1032,568 484,568" fill="url(#truck-tone)" stroke="var(--paper)" stroke-width="7"/>
      </g>
      <g role="img" aria-label="Photo of a fire-damaged yellow excavator">
        <polygon points="572,574 1032,574 1032,772 534,772" fill="url(#excavator-tone)" stroke="var(--paper)" stroke-width="7"/>
      </g>
      <g role="img" aria-label="Photo of a yellow bulldozer working in mud">
        <polygon points="648,800 1032,800 1032,974 614,974" fill="url(#dozer-tone)" stroke="var(--paper)" stroke-width="7"/>
      </g>
    </svg>

    <div class="brand">
      <span class="brand-mark"></span>
      <span class="brand-name">Gantry<br>Reclaim</span>
    </div>

    <h1 class="headline">
      <span class="accent">Trusted</span>
      <span class="accent">Insurance</span>
      <span class="plain">Auction</span>
      <span class="plain">Site for:</span>
    </h1>

    <ul class="category-list">
      <li><svg viewBox="0 0 22 22"><circle cx="11" cy="11" r="9" fill="none" stroke="var(--orange)" stroke-width="2"/><path d="M6.5 11.2l3 3 6-6.5" fill="none" stroke="var(--orange)" stroke-width="2.2" stroke-linecap="round" stroke-linejoin="round"/></svg>Semi Trucks</li>
      <li><svg viewBox="0 0 22 22"><circle cx="11" cy="11" r="9" fill="none" stroke="var(--orange)" stroke-width="2"/><path d="M6.5 11.2l3 3 6-6.5" fill="none" stroke="var(--orange)" stroke-width="2.2" stroke-linecap="round" stroke-linejoin="round"/></svg>Semi Trailers</li>
      <li><svg viewBox="0 0 22 22"><circle cx="11" cy="11" r="9" fill="none" stroke="var(--orange)" stroke-width="2"/><path d="M6.5 11.2l3 3 6-6.5" fill="none" stroke="var(--orange)" stroke-width="2.2" stroke-linecap="round" stroke-linejoin="round"/></svg>Trailers</li>
      <li><svg viewBox="0 0 22 22"><circle cx="11" cy="11" r="9" fill="none" stroke="var(--orange)" stroke-width="2"/><path d="M6.5 11.2l3 3 6-6.5" fill="none" stroke="var(--orange)" stroke-width="2.2" stroke-linecap="round" stroke-linejoin="round"/></svg>ATV/UTV</li>
      <li><svg viewBox="0 0 22 22"><circle cx="11" cy="11" r="9" fill="none" stroke="var(--orange)" stroke-width="2"/><path d="M6.5 11.2l3 3 6-6.5" fill="none" stroke="var(--orange)" stroke-width="2.2" stroke-linecap="round" stroke-linejoin="round"/></svg>Boats</li>
      <li><svg viewBox="0 0 22 22"><circle cx="11" cy="11" r="9" fill="none" stroke="var(--orange)" stroke-width="2"/><path d="M6.5 11.2l3 3 6-6.5" fill="none" stroke="var(--orange)" stroke-width="2.2" stroke-linecap="round" stroke-linejoin="round"/></svg>RVs</li>
      <li><svg viewBox="0 0 22 22"><circle cx="11" cy="11" r="9" fill="none" stroke="var(--orange)" stroke-width="2"/><path d="M6.5 11.2l3 3 6-6.5" fill="none" stroke="var(--orange)" stroke-width="2.2" stroke-linecap="round" stroke-linejoin="round"/></svg>Farm Equipment</li>
      <li><svg viewBox="0 0 22 22"><circle cx="11" cy="11" r="9" fill="none" stroke="var(--orange)" stroke-width="2"/><path d="M6.5 11.2l3 3 6-6.5" fill="none" stroke="var(--orange)" stroke-width="2.2" stroke-linecap="round" stroke-linejoin="round"/></svg>Construction Equipment</li>
    </ul>

    <div class="cta">
      <p class="cta-text">Register today for<br>a buyers account!</p>
    </div>
  </main>
</body>
</html>
```